Redesign our business card for more impact

We want to completely replace the back design of our card, and refresh or even change the front entirely. We are happy with our black Q7 logo and do not want to change it.
Our company address changed too. It is now 58 Corvallen, Irvine, CA 92741
Updates

It was reported by Sketch Harbor email today that the uploaded files didnt upload. I am trying again.

Target Market(s)

Architects and Building Owners (People making multi-million dollar decisions)

Industry/Entity Type

Consulting Engineering

Contact Information for Business Card

Contact info on the front. "wallpaper" design on back with tag line on the back "Engineering Your Future"

Font styles to use
Sans Serif

Requirements
Must have
• A vivid, modern, impactful ...but tasteful back of card design. It should communicate our premier status, but grab attention as innovative. DESIGN SHOULD BE ELEGANT AND NOT TOO BUSY.
Nice to have
• Repeating pattern, multi-color, something creative...
Should not have
• Anything that looks too playful or that we are not serious professionals. It should also not be too boring or conservative.

```html
<!DOCTYPE html>
<html lang="en">
<head>
<meta charset="utf-8">
<title>Q7 Engineering – Business Card</title>
<link rel="stylesheet" href="https://fonts.googleapis.com/css2?family=Montserrat:wght@400;800&family=Open+Sans:ital,wght@1,400;1,700&family=Russo+One&display=swap">
<style>
  :root {
    --backdrop: #161616;
    --card: #f3f2ec;
    --card-edge: #e2e1da;
    --ink: #3a3a3a;
    --line: #2b2b2b;
    --accent: #e0313f;
    --band: #5a5a5a;
    --grid: rgba(43,43,43,.07);
  }
  * { margin: 0; padding: 0; box-sizing: border-box; }
  html, body { width: 1200px; height: 889px; overflow: hidden; }
  body {
    background: var(--backdrop);
    position: relative;
    font-family: "Open Sans", sans-serif;
    color: var(--ink);
  }
  .card {
    position: absolute;
    width: 560px;
    height: 320px;
    left: 320px;
    background: radial-gradient(ellipse at 50% 40%, #fbfaf3 0%, var(--card) 60%, var(--card-edge) 100%);
    box-shadow: 0 12px 30px rgba(0,0,0,.6);
    overflow: hidden;
  }
  .card svg { position: absolute; inset: 0; }
  .card--back { top: 100px; }
  .card--front { top: 470px; }

  .wordmark {
    position: absolute;
    left: 195px; top: 65px; width: 170px; height: 170px;
    display: flex; align-items: center; justify-content: center;
    font-family: "Montserrat", sans-serif;
    font-weight: 800;
    font-size: 84px;
    color: var(--ink);
    background: var(--card);
  }
  .tagline {
    position: absolute;
    left: 0; right: 0; top: 262px;
    text-align: center;
    font-family: "Montserrat", sans-serif;
    font-weight: 400;
    font-size: 15px;
    letter-spacing: .45em;
    color: var(--ink);
  }

  .name-band {
    position: absolute;
    left: 140px; top: 52px; width: 280px; height: 62px;
    background: var(--accent);
    display: flex; align-items: center; justify-content: center;
  }
  .name {
    font-family: "Russo One", sans-serif;
    font-weight: 400;
    font-size: 25px;
    color: #fff;
    text-transform: uppercase;
    letter-spacing: .02em;
    white-space: nowrap;
  }
  .credentials {
    position: absolute;
    left: 0; right: 0; top: 126px;
    text-align: center;
    font-weight: 700; font-style: italic;
    font-size: 14px; line-height: 19px;
  }
  .contact {
    position: absolute;
    left: 0; right: 0; top: 192px;
    text-align: center;
    font-style: italic;
    font-size: 13px; line-height: 21px;
  }
</style>
</head>
<body>

  <section class="card card--back" aria-label="Card back">
    <svg width="560" height="320" viewBox="0 0 560 320">
      <defs>
        <pattern id="wallpaper-grid" width="40" height="40" patternUnits="userSpaceOnUse">
          <path d="M40 0H0V40" fill="none" stroke="var(--grid)" stroke-width="1"/>
          <rect x="18" y="18" width="4" height="4" fill="var(--grid)"/>
        </pattern>
      </defs>
      <rect class="wallpaper" width="560" height="320" fill="url(#wallpaper-grid)"/>
      <line x1="0" y1="105" x2="175" y2="140" stroke="var(--line)" stroke-width="1.2"/>
      <rect x="155" y="120" width="40" height="40" fill="var(--accent)"/>
      <circle cx="175" cy="140" r="3.5" fill="none" stroke="var(--line)" stroke-width="1.2"/>
      <rect x="400" y="195" width="40" height="40" fill="var(--accent)"/>
      <circle cx="420" cy="215" r="3.5" fill="none" stroke="var(--line)" stroke-width="1.2"/>
      <line x1="420" y1="215" x2="560" y2="250" stroke="var(--line)" stroke-width="1.2"/>
    </svg>
    <div class="wordmark">Q7</div>
    <svg width="560" height="320" viewBox="0 0 560 320" aria-hidden="true">
      <rect class="logo-frame" x="195" y="65" width="170" height="170" fill="none" stroke="var(--line)" stroke-width="1.2"/>
    </svg>
    <p class="tagline">ENGINEERING YOUR FUTURE</p>
  </section>

  <section class="card card--front" aria-label="Card front">
    <svg width="560" height="320" viewBox="0 0 560 320">
      <polyline points="62,18 62,142 145,142" fill="none" stroke="var(--line)" stroke-width="1.5"/>
      <polyline points="498,60 498,198 415,198" fill="none" stroke="var(--line)" stroke-width="1.5"/>
      <rect class="footer-band" x="120" y="282" width="320" height="38" fill="var(--band)"/>
      <line x1="165" y1="262" x2="165" y2="320" stroke="var(--accent)" stroke-width="1.5"/>
      <line x1="405" y1="270" x2="405" y2="320" stroke="var(--accent)" stroke-width="1.5"/>
    </svg>
    <div class="name-band"><h1 class="name">Daniel Reyes, PE</h1></div>
    <p class="credentials">HFDP, LEED AP<br>CEO/Principal</p>
    <p class="contact">daniel.reyes@q7eng.com<br>(555) 014-2291<br>q7eng.com<br>58 Corvallen, Irvine, CA 92741</p>
  </section>

</body>
</html>
```